KB Rubbish Removal Business Card

Hey,
I need a double sided business card designed for a rubbish removal business based in Australia. Logo is already chosen, similar colours preferred for both sides of the business card.

Details to include:

Front:

KB Rubbish Removal
Darren Holloway
Managing Director
Mobile: 0471 902 146
Email: darren@kbrubbishremoval.com.au
Website: kbrubbishremoval.com.au

Rear:

How did we do?
kbrubbishremoval.com.au/review

```html
<!DOCTYPE html>
<html lang="en">
<head>
<meta charset="utf-8">
<title>KB Rubbish Removal – Business Card</title>
<link href="https://fonts.googleapis.com/css2?family=Roboto:wght@400;500&display=swap" rel="stylesheet">
<style>
  :root {
    --page-bg: #dadada;
    --card-white: #ffffff;
    --brand-green: #0cd35a;
    --text-grey: #474747;
    --back-light: #8a8a8a;
    --back-mid: #2e2e2e;
    --back-dark: #141414;
    --back-text: #e6e6e6;
  }
  * { margin: 0; padding: 0; box-sizing: border-box; }
  html, body {
    width: 1200px; height: 1200px; overflow: hidden;
    background: var(--page-bg);
    font-family: "Roboto", Arial, sans-serif;
  }
  .card {
    position: absolute;
    left: 218px;
    width: 763px;
    height: 437px;
    overflow: hidden;
  }
  .card--front { top: 115px; background: var(--card-white); }
  .card--back  { top: 648px; background: var(--back-mid); }

  /* Front */
  .brand-mark {
    position: absolute; left: 50px; top: 43px;
    width: 84px; height: 84px; border-radius: 50%;
    background: var(--brand-green);
  }
  .brand-name {
    position: absolute; right: 48px; top: 58px;
    font-weight: 500; font-size: 54px; line-height: 1;
    color: var(--brand-green);
    text-transform: uppercase;
    white-space: nowrap;
  }
  .person {
    position: absolute; right: 50px; top: 206px; text-align: right;
  }
  .person__name {
    font-weight: 500; font-size: 34px; line-height: 1;
    color: var(--brand-green); text-transform: uppercase;
    letter-spacing: 0.6px;
  }
  .person__title {
    margin-top: 5px;
    font-size: 19px; line-height: 1.1; color: var(--text-grey);
  }
  .divider {
    position: absolute; left: 50px; top: 273px;
    width: 665px; height: 1px; background: var(--brand-green);
  }
  .edge-tab {
    position: absolute; right: 0; top: 214px;
    width: 11px; height: 44px; background: var(--brand-green);
  }
  .contacts {
    position: absolute; left: 50px; top: 320px;
    list-style: none;
  }
  .contacts li {
    display: flex; align-items: center; gap: 6px;
    height: 25px;
    font-size: 20px; color: var(--text-grey);
  }
  .contacts svg { width: 12px; height: 12px; flex: none; }

  /* Back */
  .back-texture {
    position: absolute; inset: 0;
    background: linear-gradient(120deg, var(--back-light) 0%, #555 30%, var(--back-mid) 55%, var(--back-dark) 100%);
  }
  .back-mark {
    position: absolute; left: 355px; top: 178px;
    width: 53px; height: 53px; border-radius: 50%;
    background: var(--brand-green);
  }
  .review {
    position: absolute; left: 0; right: 0; top: 256px;
    text-align: center; color: var(--back-text);
  }
  .review__ask { font-weight: 500; font-size: 22px; line-height: 1.2; }
  .review__url { margin-top: 6px; font-size: 17px; line-height: 1.2; color: var(--brand-green); }
</style>
</head>
<body>

<section class="card card--front">
  <div class="brand-mark" aria-hidden="true"></div>
  <h1 class="brand-name">KB Rubbish Removal</h1>

  <div class="person">
    <p class="person__name">Darren Holloway</p>
    <p class="person__title">Managing Director</p>
  </div>
  <div class="divider"></div>
  <div class="edge-tab"></div>

  <ul class="contacts">
    <li>
      <svg viewBox="0 0 12 12" aria-hidden="true"><path d="M2.5 1 L4.5 1 L5 3.5 L3.8 4.5 Q5 7.5 7.5 8.2 L8.5 7 L11 7.5 L11 9.5 Q10.5 11 9 11 Q2 10 1 3 Q1 1.5 2.5 1 Z" fill="none" stroke="#0cd35a" stroke-width="1.2"/></svg>
      <span>0471 902 146</span>
    </li>
    <li>
      <svg viewBox="0 0 12 12" aria-hidden="true"><rect x="0.8" y="2.3" width="10.4" height="7.4" fill="none" stroke="#0cd35a" stroke-width="1.2"/><path d="M1 2.6 L6 6.5 L11 2.6" fill="none" stroke="#0cd35a" stroke-width="1.2"/></svg>
      <span>darren@kbrubbishremoval.com.au</span>
    </li>
    <li>
      <svg viewBox="0 0 12 12" aria-hidden="true"><circle cx="6" cy="6" r="5" fill="none" stroke="#0cd35a" stroke-width="1"/><ellipse cx="6" cy="6" rx="2.2" ry="5" fill="none" stroke="#0cd35a" stroke-width="1"/><path d="M1 6 H11 M2 3.5 H10 M2 8.5 H10" stroke="#0cd35a" stroke-width="0.9"/></svg>
      <span>www.kbrubbishremoval.com.au</span>
    </li>
  </ul>
</section>

<section class="card card--back">
  <div class="back-texture" role="img" aria-label="Repeating embossed brand-mark pattern fading from light grey to black"></div>
  <div class="back-mark" aria-hidden="true"></div>
  <div class="review">
    <p class="review__ask">How did we do?</p>
    <p class="review__url">kbrubbishremoval.com.au/review</p>
  </div>
</section>

</body>
</html>
```